Gobal construction supply company needs new business card design

I need a business card design for my global supply company using an existing logo. i will be looking to print these on rounded corner cards with the black background version of my logo on the back. on the front white background, my logo again and my simple details.

```html
<!DOCTYPE html>
<html lang="en">
<head>
<meta charset="utf-8">
<title>Meridian Build Supply – Business Card</title>
<link href="https://fonts.googleapis.com/css2?family=Roboto:wght@400;500;700&display=swap" rel="stylesheet">
<style>
  :root {
    --backdrop: #2b2b2b;
    --card-white: #f3f3f3;
    --card-black: #1c1c1c;
    --ink: #141414;
    --ink-soft: #4a4a4a;
    --accent: #d40000;
    --divider: #c9c9c9;
    --light: #f4f4f4;
  }
  html, body {
    margin: 0;
    padding: 0;
    width: 1200px;
    height: 960px;
    overflow: hidden;
    background: var(--backdrop);
    font-family: "Roboto", Arial, sans-serif;
  }
  .canvas {
    position: relative;
    width: 1200px;
    height: 960px;
  }
  .card {
    position: absolute;
    left: 310px;
    width: 600px;
    border-radius: 18px;
    overflow: hidden;
    box-shadow: 0 8px 18px rgba(0,0,0,0.45);
  }
  /* Front */
  .card-front {
    top: 113px;
    height: 334px;
    background: var(--card-white);
  }
  .card-front .edge-line {
    position: absolute;
    left: 0; right: 0;
    bottom: 6px;
    height: 2px;
    background: var(--accent);
  }
  .card-front .edge-base {
    position: absolute;
    left: 0; right: 0; bottom: 0;
    height: 6px;
    background: #e9e9e9;
  }
  .brand-block {
    position: absolute;
    left: 40px;
    top: 112px;
    width: 250px;
    text-align: center;
  }
  .brand-dot {
    display: block;
    width: 20px;
    height: 20px;
    margin: 0 auto 14px;
    border-radius: 50%;
    background: var(--accent);
  }
  .brand-name {
    font-weight: 500;
    font-size: 19px;
    letter-spacing: 0.4px;
    color: var(--ink);
    white-space: nowrap;
  }
  .divider {
    position: absolute;
    left: 307px;
    top: 72px;
    width: 1px;
    height: 198px;
    background: var(--divider);
  }
  .details {
    position: absolute;
    left: 331px;
    top: 73px;
    color: var(--ink-soft);
  }
  .person-name {
    margin: 0;
    font-weight: 700;
    font-size: 22px;
    line-height: 26px;
    color: var(--ink);
    letter-spacing: 0.3px;
  }
  .person-role {
    margin: 0;
    font-weight: 500;
    font-size: 15px;
    line-height: 18px;
    color: var(--accent);
  }
  .address {
    margin: 10px 0 0;
    font-size: 14.5px;
    line-height: 19px;
    font-style: normal;
  }
  .contact-list {
    list-style: none;
    margin: 10px 0 0;
    padding: 0;
    font-size: 14.5px;
    line-height: 19px;
  }
  .contact-list li {
    display: flex;
    align-items: center;
    gap: 9px;
  }
  .contact-list svg {
    width: 13px;
    height: 13px;
    fill: var(--ink);
    flex: none;
  }
  /* Back */
  .card-back {
    top: 511px;
    height: 342px;
    background: var(--card-black);
  }
  .back-brand {
    position: absolute;
    left: 0; right: 0;
    top: 110px;
    text-align: center;
  }
  .back-brand .brand-dot {
    width: 36px;
    height: 36px;
    margin-bottom: 22px;
  }
  .back-brand .brand-name {
    font-size: 38px;
    color: var(--light);
    letter-spacing: 1px;
  }
  .back-web {
    position: absolute;
    left: 0; right: 0;
    top: 290px;
    text-align: center;
    font-size: 15px;
    letter-spacing: 3px;
    color: var(--light);
  }
</style>
</head>
<body>
<div class="canvas">
  <section class="card card-front">
    <div class="brand-block">
      <span class="brand-dot"></span>
      <div class="brand-name">MERIDIAN BUILD SUPPLY</div>
    </div>
    <div class="divider"></div>
    <div class="details">
      <h1 class="person-name">DANIEL MARSH</h1>
      <p class="person-role">CEO/FOUNDER</p>
      <address class="address">214 Harbor Street<br>Portland, Oregon 97201</address>
      <ul class="contact-list">
        <li><svg viewBox="0 0 24 24"><path d="M6.6 10.8a15.1 15.1 0 0 0 6.6 6.6l2.2-2.2c.3-.3.7-.4 1-.2 1.1.4 2.3.6 3.6.6.6 0 1 .4 1 1V20c0 .6-.4 1-1 1A17 17 0 0 1 3 4c0-.6.4-1 1-1h3.5c.6 0 1 .4 1 1 0 1.3.2 2.5.6 3.6.1.3 0 .7-.2 1z"/></svg>503 210 4471</li>
        <li><svg viewBox="0 0 24 24"><path d="M7 1h10a2 2 0 0 1 2 2v18a2 2 0 0 1-2 2H7a2 2 0 0 1-2-2V3a2 2 0 0 1 2-2zm0 3v14h10V4zm5 15.5a1.2 1.2 0 1 0 0 2.4 1.2 1.2 0 0 0 0-2.4z"/></svg>503 388 6120</li>
        <li><svg viewBox="0 0 24 24"><path d="M6 2h10l2 2v5H6zm-3 8h18a2 2 0 0 1 2 2v7h-4v3H5v-3H1v-7a2 2 0 0 1 2-2zm4 7v3h10v-3z"/></svg>503 210 4472</li>
        <li><svg viewBox="0 0 24 24"><path d="M2 5h20v14H2zm2 2v.5l8 5.5 8-5.5V7zm0 3v7h16v-7l-8 5.5z"/></svg>daniel@meridianbuild.com</li>
        <li><svg viewBox="0 0 24 24"><path d="M12 2a10 10 0 1 0 0 20 10 10 0 0 0 0-20zm-1 17.9A8 8 0 0 1 4.2 10.2L9 15v1a2 2 0 0 0 2 2zm6.9-2.5A2 2 0 0 0 16 16h-1v-3a1 1 0 0 0-1-1H8v-2h2a1 1 0 0 0 1-1V7h2a2 2 0 0 0 2-2v-.4a8 8 0 0 1 2.9 12.8z"/></svg>www.meridianbuild.com</li>
      </ul>
    </div>
    <div class="edge-line"></div>
    <div class="edge-base"></div>
  </section>

  <section class="card card-back">
    <div class="back-brand">
      <span class="brand-dot"></span>
      <div class="brand-name">MERIDIAN BUILD SUPPLY</div>
    </div>
    <div class="back-web">www.meridianbuild.com</div>
  </section>
</div>
</body>
</html>
```